Covid 19 Exit Strategy one page brochure

I would like to design, and will need URGENT help, a brochure detailing a Covid 19 Exit Strategy plan. This brochure will need to be understood easily and the graphics inside should make it easy for people to understand without reading the entire text. This project is quite urgent and needs to be completed THIS WEEK - by Saturday may 16th at the latest. I am attaching two examples. I will provide the text.

```html
<!DOCTYPE html>
<html lang="en">
<head>
<meta charset="utf-8">
<title>COVID-19 Phased Social &amp; Economical Restart</title>
<link href="https://fonts.googleapis.com/css2?family=Montserrat:wght@300;400;500;600;700;800&display=swap" rel="stylesheet">
<style>
:root{
  --backdrop:#7c7b86;
  --paper:#ffffff;
  --teal:#02b2d3;
  --teal-text:#1aa9c9;
  --red:#cd1f35;
  --ink:#1d1d1f;
  --white:#ffffff;
}
*{box-sizing:border-box;margin:0;padding:0}
html,body{width:1200px;height:2970px;overflow:hidden}
body{background:var(--backdrop);font-family:"Montserrat",sans-serif;color:var(--ink);position:relative}
.page{position:absolute;left:52px;width:1089px;background:var(--paper);overflow:hidden;box-shadow:0 2px 6px rgba(0,0,0,.35)}
.page-one{top:43px;height:1409px}
.page-two{top:1522px;height:1409px}
.abs{position:absolute}
.title{left:31px;top:50px;font-size:60px;font-weight:400;letter-spacing:1px;line-height:1}
.subtitle{left:31px;top:111px;font-size:29px;font-weight:400;line-height:1}
.tagline{left:31px;top:152px;font-size:29px;font-weight:400;color:var(--teal-text);line-height:1}
.author-bar{left:31px;top:197px;width:541px;height:53px;background:var(--teal);color:var(--white);font-size:29px;font-weight:700;display:flex;align-items:center;justify-content:center;letter-spacing:.5px}
.intro{left:31px;top:264px;width:547px;font-size:11.6px;line-height:15px;text-align:justify}
.rule{left:29px;top:426px;width:63px;height:4px;background:var(--red)}
.section-heading{left:29px;top:439px;font-size:20px;font-weight:800;letter-spacing:-.2px}
.portrait{left:596px;top:130px;width:490px;height:520px}
.item{position:absolute;font-size:11.5px;line-height:14.8px;text-align:justify;padding-left:52px}
.item .icon{position:absolute;left:0;top:-2px;width:42px;height:42px;border-radius:50%;background:var(--white);border:2px solid var(--red);display:flex;align-items:center;justify-content:center}
.item .icon::after{content:"";width:17px;height:17px;border-radius:4px;border:2px solid var(--red)}
.band-teal{background:var(--teal);color:var(--white)}
.band-red{background:var(--red);color:var(--white)}
.band-teal .item,.band-red .item{color:var(--white)}
.band-teal .icon,.band-red .icon{border-color:var(--white)}
.strategy-band{left:0;top:846px;width:1089px;height:563px}
.strategy-title{left:0;top:29px;width:1089px;text-align:center;font-size:20px;font-weight:700;letter-spacing:9.5px;color:var(--white)}
.stage-box{position:absolute;display:flex;align-items:center}
.stage-box .label{font-size:30px;font-weight:800;padding:0 14px 0 40px;position:relative;white-space:nowrap}
.stage-box .label::before{content:"";position:absolute;left:0;top:50%;margin-top:-10px;border-top:10px solid transparent;border-bottom:10px solid transparent;border-left:12px solid var(--teal)}
.stage-box .desc{border-left:2px solid currentColor;padding:0 10px;font-size:11.5px;line-height:14.5px}
.stage-box .desc strong{font-weight:700}
.stage-one{left:162px;top:63px;width:746px;height:60px;background:var(--white);color:var(--teal)}
.stage-one .desc{color:var(--ink);border-left-color:var(--teal)}
.stage-two{left:151px;top:27px;width:746px;height:59px;background:var(--red);color:var(--white)}
.stage-two .label::before{border-left-color:var(--white)}
.stage-three{left:96px;top:17px;width:902px;height:81px;background:var(--white);color:var(--red)}
.stage-three .label::before{border-left-color:var(--red)}
.stage-three .desc{color:var(--ink);border-left-color:var(--red)}
.continuation{left:0;top:0;width:1089px;height:213px}
.stage-two-area{left:0;top:213px;width:1089px;height:669px}
.stage-three-area{left:0;top:882px;width:1089px;height:527px}
</style>
</head>
<body>

<section class="page page-one">
  <h1 class="abs title">COVID-19</h1>
  <p class="abs subtitle">Phased Social &amp; Economical Restart</p>
  <p class="abs tagline">A Global Benchmark of Best Practices</p>
  <div class="abs author-bar">LENA ARVID</div>
  <p class="abs intro">Pandemics have, historically, seen their end both medically - via herd immunity or immunizations. And while there are several clinical trials underway for potential Covid-19 vaccines, we are still a long way from deploying an effective vaccine and one that will stand the test of time as the virus changes. Covid-19 pandemic will be considered 'ended' when there are only occasional traces of localized cases that are quickly contained in specific locations., Today and in the absence of an effective vaccine(s) and for the re-opening of the economies and social activities to be successful, it is critical that the following basic conditions be in place before any lockdowns are lifted and before social activities resume:</p>

  <svg class="abs portrait" viewBox="0 0 490 520" role="img" aria-label="Photo of a woman in a white top wearing a surgical mask and applying hand sanitiser">
    <defs>
      <linearGradient id="photoTone" x1="0" y1="0" x2="0" y2="1">
        <stop offset="0" stop-color="#e9e6e2"/>
        <stop offset="1" stop-color="#cfcac4"/>
      </linearGradient>
    </defs>
    <path d="M20 70 C60 10 150 20 200 40 C280 0 420 20 470 120 C500 190 470 260 450 320 C420 420 330 510 230 500 C120 490 40 420 20 310 C0 220 -10 130 20 70 Z" fill="var(--teal)"/>
    <path d="M8 100 C10 50 60 30 95 60 C120 90 100 150 60 160 C25 165 6 140 8 100 Z" fill="var(--red)"/>
    <circle cx="255" cy="285" r="235" fill="url(#photoTone)"/>
  </svg>

  <div class="abs rule"></div>
  <h2 class="abs section-heading">GENERAL REQUIREMENTS</h2>

  <div class="item" style="left:31px;top:495px;width:259px"><span class="icon"></span>Single digit downward trend of documented cases within the past 14- days.</div>
  <div class="item" style="left:31px;top:581px;width:259px"><span class="icon"></span>Ability to screen and test symptomatic individuals within 24 hours of identification. Increased and sufficient testing capacity, to test at least 50% of all population if necessary within a timeframe of 3 months.</div>
  <div class="item" style="left:31px;top:720px;width:259px"><span class="icon"></span>Ability to track and trace infected patients and contacts on a live basis and across the country and ability to react quickly to any unusual trends or outbreaks.</div>

  <div class="item" style="left:328px;top:495px;width:256px"><span class="icon"></span>Hospitals and the health care system are capable of treating patients without operating on a crisis mode.</div>
  <div class="item" style="left:328px;top:574px;width:256px"><span class="icon"></span>Ability to surge ICU capacity on a short notice - 24h.</div>
  <div class="item" style="left:328px;top:645px;width:420px;text-align:left"><span class="icon"></span>Plan in place to trigger targeted or full-scale containment in case of sudden outbreaks</div>
  <div class="item" style="left:328px;top:720px;width:445px"><span class="icon"></span>Mandatory use of masks (at least surgical grade) for everyone in all public areas and at work. Mandatory use of N95, or equivalent, masks for all healthcare front workers and for all government agencies and authorities that are involved in overseeing the containment activities.</div>

  <div class="item" style="left:807px;top:628px;width:256px"><span class="icon"></span>Mandatory daily checks of body temperature for everyone at the workplace or entering public areas.</div>
  <div class="item" style="left:807px;top:720px;width:256px"><span class="icon"></span>Mandatory sanitation in all places - use of disinfection available on a large scale.</div>

  <div class="abs strategy-band band-teal">
    <h2 class="abs strategy-title">PHASED COVID-19 LOCKDOWN EXIT STRATEGY PLAN</h2>
    <div class="stage-box stage-one">
      <div class="label">STAGE 1</div>
      <p class="desc">To enter this stage, additional to the general requirements, the Effective Reproduction Number (Rt) must be less than 1 and the death rate at less than 3%.<br><strong>The economy and social activities can resume in this sequence:</strong></p>
    </div>

    <div class="item" style="left:31px;top:177px;width:259px"><span class="icon"></span>Elderly (60+ years old) and vulnerable individuals should continue to self-isolate.</div>
    <div class="item" style="left:31px;top:235px;width:259px"><span class="icon"></span>No more than 5 people maximum gathering at a time in public areas and at work.</div>
    <div class="item" style="left:31px;top:314px;width:259px"><span class="icon"></span>Work from home should continue whenever and as much as possible.</div>
    <div class="item" style="left:31px;top:387px;width:259px"><span class="icon"></span>Social distancing should continue to be re-enforced in public areas, at work and in all areas reopened.</div>
    <div class="item" style="left:31px;top:472px;width:259px"><span class="icon"></span>Non-essential travel should be minimized between cities and regions (and within cities and regions where covid-19 infections are still a risk)</div>

    <div class="item" style="left:328px;top:177px;width:362px"><span class="icon"></span>Large businesses (300 people and more, manufacturing, services, etc.) can reopen progressively. Common areas should remain closed (cafeteria, restaurant, gym, meeting rooms of no more than 5 people).</div>
    <div class="item" style="left:328px;top:277px;width:362px"><span class="icon"></span>Small businesses (300 people and less) can reopen as well with the same conditions as large businesses.</div>
    <div class="item" style="left:328px;top:348px;width:362px"><span class="icon"></span>Commercial shops can reopen. Shops should control the flow of people in their facilities not to exceed 30% at a time of standard capacity. Shops should provide disinfectant and temperature control at entry.</div>
    <div class="item" style="left:328px;top:445px;width:362px"><span class="icon"></span>Pharmacies will continue to be open. However, they must make available disinfectant for use by clients and will continue to comply with social distancing. Pharmacies should limit the number of client/patient in their stores not to exceed 30% of the standard capacity.</div>

    <div class="item" style="left:711px;top:177px;width:351px"><span class="icon"></span>Transportation (buses, taxis, airlines) will resume progressively. No air travels permitted in and out of Covid-19 known hotspots, locally or internationally. Entry to country should be limited and strictly controlled. All landing passengers and visitors regardless of the country of origin should be tested for Covid-19 at arrival. All passengers and visitors will undergo a temperature check at arrival. No more than 3 people at a time in a taxi/Rydo including the driver. All passengers wearing masks. Buses should operate with no more than 30% customer's capacity per bus.</div>
    <div class="item" style="left:720px;top:436px;width:351px;padding-left:53px"><span class="icon"></span>Religious sites can reopen with a maximum capacity of 30% or less. Social distancing and wearing masks is mandatory. Religious sites should organize (volunteers can help) to check body temperature of everyone accessing the site and provide disinfectant at entry.</div>
  </div>
</section>

<section class="page page-two">
  <div class="abs continuation band-teal">
    <div class="item" style="left:29px;top:45px;width:463px"><span class="icon"></span>Hotels &amp; tourism (museums, etc.) can reopen but must operate at 30% or less capacity. All common areas (restaurants, gyms, swimming pools, conference rooms, etc.) should remain closed.</div>
    <div class="item" style="left:29px;top:128px;width:463px"><span class="icon"></span>Coffee &amp; restaurants can reopen but must operate at 30% capacity as well and comply with social distancing. Clients must wear as much as possible their masks if they are not consuming food/coffee. Clients should avoid to talking to each other with masks off.</div>
    <div class="item" style="left:573px;top:45px;width:489px"><span class="icon"></span>All schools should remain closed. On-line courses should continue be the preferred method for education</div>
    <div class="item" style="left:573px;top:128px;width:489px"><span class="icon"></span>Large scale events (cinema, theaters, sport, business conferences, etc.) should remain closed or operate virtually. Sport events can resume but without spectators. Athletes and the staff surrounding them should be tested, disinfectants should be available and masks used as much as reasonably possible.</div>
  </div>

  <div class="abs stage-two-area">
    <div class="stage-box stage-two">
      <div class="label">STAGE 2</div>
      <p class="desc">To enter this stage, additional to the general requirements, the Effective Reproduction Number (Rt) must be less than 1 and the death rate at less than 3%.<br><strong>The economy and social activities can resume in this sequence:</strong></p>
    </div>

    <div class="item" style="left:31px;top:124px;width:255px"><span class="icon"></span>Elderly (60+ years old) and vulnerable individuals should continue to self-isolate as much as possible.</div>
    <div class="item" style="left:31px;top:268px;width:255px"><span class="icon"></span>No more than 10 people maximum gathering at a time in public areas and at work.</div>
    <div class="item" style="left:31px;top:378px;width:255px"><span class="icon"></span>Work from home should if possible or for jobs that do not have to be necessarily in an office setup.</div>
    <div class="item" style="left:31px;top:495px;width:255px"><span class="icon"></span>Social distancing can be relaxed. However people should continue to wear masks and use disinfectants</div>
    <div class="item" style="left:31px;top:606px;width:255px"><span class="icon"></span>Travel can resume between cities and regions. The same containment restrictions should apply to any existing hotspot.</div>

    <div class="item" style="left:315px;top:124px;width:257px"><span class="icon"></span>Elective surgeries can resume in hospitals and clinics that are equipped to comply with all general requirements.</div>
    <div class="item" style="left:315px;top:238px;width:257px"><span class="icon"></span>Large businesses (300 people and more, manufacturing, services, etc.) will continue to operate. Common areas should open but social distancing should remain (cafeteria, restaurant, gym, meeting rooms of no more than 10 people).</div>
    <div class="item" style="left:315px;top:398px;width:257px"><span class="icon"></span>Small businesses (300 people and less) will continue to operate with the same conditions as large businesses.</div>
    <div class="item" style="left:315px;top:505px;width:257px"><span class="icon"></span>Commercial shops will continue to be open and can operate at 50% capacity. Wear of masks should continue.</div>
    <div class="item" style="left:315px;top:606px;width:257px"><span class="icon"></span>Pharmacies will continue to be open and will need to operate a 50% capacity</div>

    <div class="item" style="left:623px;top:124px;width:436px"><span class="icon"></span>Transportation (buses, taxis, and airlines) will continue to operate. Still no air travels permitted in and out of Covid-19 known hotspots, locally or internationally. Entry to country should be relaxed but remain controlled. Airports should continue to use thermo cameras to monitor passenger's temperature at landing. Airports should be equipped to test for Covid-19 if necessary. Transportation by taxi/Rydo continues, however, passengers wear masks. Buses could operate with 50% capacity per bus.</div>
    <div class="item" style="left:623px;top:283px;width:436px"><span class="icon"></span>Religious sites can operate with a maximum capacity of 50%. Social distancing and wearing masks should be enforced. Sites should continue to check body temperature of everyone accessing the site and provide disinfectant at entry.</div>
    <div class="item" style="left:623px;top:365px;width:436px"><span class="icon"></span>Hotels &amp; tourism (museums, etc.) can operate at 50% capacity. All common areas (restaurants, gyms, swimming pools, conference rooms, etc.) could reopen. Gatherings are limited to 10 people or less and can be expanded with social distancing and wearing protective masks.</div>
    <div class="item" style="left:623px;top:458px;width:436px"><span class="icon"></span>Coffee &amp; restaurants can operate at 50% capacity and continue comply with social distancing. Clients must wear as much as possible their masks if they are not consuming food/coffee.</div>
    <div class="item" style="left:623px;top:540px;width:436px"><span class="icon"></span>Schools can reopen in parallel with on-line education. Social distancing and re-arranging school seating to prevent the spread of infection is mandatory</div>
    <div class="item" style="left:623px;top:606px;width:436px"><span class="icon"></span>Large scale events (cinema, theaters, sport, business conferences, etc.) could resume under strict social distancing. People should wear masks.</div>
  </div>

  <div class="abs stage-three-area band-red">
    <div class="stage-box stage-three">
      <div class="label">STAGE 3</div>
      <p class="desc">To enter stage 3 of the Covid-19 Exit Strategy, compliance to the general requirements is compulsory, additional to a successful Stage 2 outcome. The Effective Reproduction Number (Rt) for Stage 3 must be less than 0.3 and the death rate stabilized at less than 1%.<br><strong>The economy and social activities can resume in this sequence:</strong></p>
    </div>

    <div class="item" style="left:31px;top:130px;width:353px;text-align:left"><span class="icon"></span>Elderly (60+ years old) and vulnerable individuals may resume all previously exercised activities without restrictions. Restrictions as to the number of people gathering together can be lifted. Social distancing can be relaxed. However, wear of masks may continue.</div>
    <div class="item" style="left:31px;top:259px;width:353px;text-align:left"><span class="icon"></span>Travel can resume between cities and regions and out of country travel. The same containment restrictions as Stage 1 and 2 would continue to apply to any existing hotspot</div>
    <div class="item" style="left:31px;top:357px;width:353px;text-align:left"><span class="icon"></span>All hospital and clinic surgeries can resume in hospitals in compliance with standard hospital and health care procedures.</div>
    <div class="item" style="left:31px;top:450px;width:353px"><span class="icon"></span>Large businesses (300 people and more, manufacturing, services, etc.) will resume normal business practices. Wear of masks is recommended but not mandatory.</div>

    <div class="item" style="left:395px;top:130px;width:353px;text-align:left"><span class="icon"></span>Small businesses (300 people and less) will operate with the same conditions as large businesses.</div>
    <div class="item" style="left:395px;top:204px;width:353px"><span class="icon"></span>Commercial shops can operate on a normal mode - previous to covid- 19. Wear of masks could be recommended in certain areas</div>
    <div class="item" style="left:395px;top:292px;width:353px;padding-left:55px"><span class="icon"></span>Pharmacies can operate at a normal state.</div>
    <div class="item" style="left:395px;top:342px;width:353px"><span class="icon"></span>Transportation (buses, taxis, and airlines) will operate at a normal capacity. Still no air travels permitted in and out of Covid-19 known hotspots, locally or internationally. Entry to country should be relaxed and operate normally. Airports should continue to use thermo cameras to monitor passenger's temperature at landing. Airports should be equipped to test for Covid-19 if necessary. Transportation by taxi/Rydo and buses will resume on a normal mode. Wear of masks is elective.</div>

    <div class="item" style="left:770px;top:130px;width:289px;text-align:left"><span class="icon"></span>Religious sites can operate normally. Wear of masks should be elective</div>
    <div class="item" style="left:770px;top:198px;width:289px;text-align:left"><span class="icon"></span>Hotels &amp; tourism (museums, etc.) can operate at 100% capacity including all common areas</div>
    <div class="item" style="left:770px;top:278px;width:289px"><span class="icon"></span>Coffee &amp; restaurants can resume normal operations. Clients may wear masks for personal protection if they wish to.</div>
    <div class="item" style="left:770px;top:364px;width:289px"><span class="icon"></span>Schools can resume operations. Re-arranging school seating should continue until a vaccine is found.</div>
    <div class="item" style="left:770px;top:437px;width:289px"><span class="icon"></span>Large scale events (cinema, theaters, sport, business conferences, etc) could resume under moderate social distancing. People may elect to wear masks.</div>
  </div>
</section>

</body>
</html>
```